New web design for a service provider in the medical field

We are looking for a new design for our website. We are a company that repairs and sells medical endoscopes. Our customers include doctors and hospitals. Our current website can be found at https://lumavend.de/en/lumavend-english.
We need a new web design (without programming) for the following 3 pages:
-Startpage https://lumavend.de/en/lumavend-english/
-Used endoscopes https://lumavend.de/en/used-endoscopes/
-Purchase https://lumavend.de/en/purchase/
The design should be modern and stylish.
The blue color of the logo should be reflected on the page, but not too intrusive.
I have uploaded the images from the header. If more images are needed, let me know and I will upload them.

Target Market(s)
Doctors and hospitals
Coding
Coded - Design and coding required
Number of Pages Required
1 page
Look and feel
Each slider illustrates characteristics of the customer's brand and the style your logo design should communicate.

```html
<!DOCTYPE html>
<html lang="en">
<head>
<meta charset="utf-8">
<title>LumaVend – Endoscope Repair &amp; Sale</title>
<link href="https://fonts.googleapis.com/css2?family=Dosis:wght@600;700&family=Roboto:wght@300;400;500;700;900&display=swap" rel="stylesheet">
<style>
:root{
  --blue:#3cb9fc;
  --blue-dark:#1ea6f2;
  --ink:#222;
  --grey:#8a8f96;
  --hero-bg:#f2f9fe;
  --soft-bg:#f5fbff;
  --footer:#232323;
  --white:#fff;
}
*{margin:0;padding:0;box-sizing:border-box}
html,body{width:1200px;height:3831px;overflow:hidden}
body{position:relative;font-family:'Roboto',sans-serif;color:var(--ink);background:var(--white)}
.abs{position:absolute}
a{color:inherit;text-decoration:none}

/* top bar */
.topbar{top:0;left:0;width:1200px;height:46px;font-size:14px}
.topbar .item{position:absolute;top:15px;display:flex;align-items:center;gap:10px}
.topbar .lang{position:absolute;top:15px;left:1055px;font-size:13px;font-weight:500}
.topbar .lang span{color:var(--blue)}
.nav{top:46px;left:0;width:1200px;height:61px;background:var(--blue)}
.brand{position:absolute;left:138px;top:10px;color:#3a3f45;font-family:'Dosis',sans-serif;font-weight:700;font-size:34px;letter-spacing:1px}
.nav a{position:absolute;top:21px;color:var(--white);font-size:15px;font-weight:500}

/* hero */
.hero{top:107px;left:0;width:1200px;height:577px;background:var(--hero-bg)}
.hero-tag{top:242px;left:107px;height:27px;padding:0 16px;line-height:27px;background:var(--blue);color:var(--white);font-size:11px}
.hero-title{top:278px;left:105px;font-weight:900;font-size:62px;line-height:75px;letter-spacing:1px;color:var(--ink)}
.hero-text{top:520px;left:107px;width:440px;font-size:13px;line-height:24px;color:#777}
.btn{position:absolute;height:43px;border-radius:22px;background:var(--blue);color:var(--white);font-size:13px;line-height:43px;text-align:center}
.photo{position:absolute}
.hero-photo{left:613px;top:268px;width:483px;height:312px;background:radial-gradient(ellipse at 60% 45%,#5a5f66,#2c2f33 45%,rgba(242,249,254,0) 72%)}

/* features */
.feature{position:absolute;top:781px;width:226px;height:104px;background:var(--white);box-shadow:0 4px 18px rgba(0,0,0,.07);text-align:center}
.feature .ic{position:absolute;left:86px;top:-25px;width:54px;height:54px;border-radius:50%;background:var(--white);border:2px solid var(--blue);border-bottom-color:transparent;border-left-color:#cdeafc;border-right-color:#cdeafc;display:flex;align-items:center;justify-content:center}
.feature h3{margin-top:43px;font-size:17px;font-weight:500}
.feature p{margin-top:6px;font-size:12px;color:var(--grey)}

/* section heads */
.sec-title{position:absolute;left:0;width:1200px;text-align:center;font-family:'Dosis',sans-serif;font-weight:700;font-size:33px;color:var(--blue)}
.sec-sub{position:absolute;left:330px;width:540px;text-align:center;font-size:12.5px;line-height:23px;color:var(--grey)}

/* services */
.svc{position:absolute}
.svc h4{font-size:16px;font-weight:500}
.svc p{margin-top:8px;font-size:12.5px;line-height:23px;color:var(--grey)}
.svc.left{left:161px;width:260px}
.svc.right{left:778px;width:260px;text-align:right}
.svc-ic{position:absolute;width:40px;height:40px}
.svc-photo{left:432px;top:1063px;width:338px;height:283px;background:linear-gradient(90deg,#bdb6aa 0%,#8f8a84 30%,#3a3d42 60%,#1d1f22 100%)}

/* blue band */
.band{top:1457px;left:0;width:1200px;height:610px;background:linear-gradient(135deg,#46bdfc 0%,#3cb9fc 55%,#62c7fc 100%)}
.band-col{position:absolute;top:1527px;width:490px;text-align:center;color:var(--white)}
.band-col h2{margin-top:40px;font-family:'Dosis',sans-serif;font-weight:700;font-size:33px}
.band-col .sub{margin-top:6px;font-size:12.5px}
.band-col p{margin-top:27px;font-size:15px;line-height:23.5px}
.divider{top:1823px;left:104px;width:992px;border-top:2px dashed rgba(255,255,255,.85)}
.diamond{top:1815px;left:592px;width:16px;height:16px;background:var(--white);transform:rotate(45deg)}
.quote-title{top:1870px;left:0;width:1200px;text-align:center;font-family:'Dosis',sans-serif;font-weight:700;font-size:44px;color:var(--white)}
.quote-btn{top:1949px;left:489px;width:222px;height:52px;border:2px dashed var(--white);border-radius:4px;color:var(--white);text-align:center;line-height:48px;font-family:'Dosis',sans-serif;font-weight:700;font-size:16px}

/* reviews */
.reviews{top:2067px;left:0;width:1200px;height:615px;background:var(--soft-bg)}
.review{position:absolute;top:2272px;width:479px;height:196px;background:var(--white);box-shadow:0 4px 18px rgba(0,0,0,.05);padding:40px 44px;font-size:15px;line-height:23.5px;color:var(--grey)}
.avatar{position:absolute;top:2443px;width:96px;height:96px;border-radius:50%;border:4px solid #d8eefc}
.rname{position:absolute;top:2493px;font-family:'Dosis',sans-serif;font-weight:700;font-size:19px}
.rrole{position:absolute;top:2522px;font-size:13px;color:var(--grey)}
.arrow{top:2578px;font-size:24px;color:var(--blue-dark)}

/* posts */
.post{position:absolute;top:2870px;width:311px;height:468px;background:var(--white);box-shadow:0 4px 18px rgba(0,0,0,.07)}
.post .img{height:220px}
.post .body{padding:25px 27px}
.post .date{font-size:11.5px;color:var(--blue)}
.post h3{margin-top:14px;font-size:19px;line-height:24px;font-weight:400;color:#333}
.post p{margin-top:12px;font-size:12.5px;line-height:23px;color:var(--grey)}
.share{display:inline-flex;align-items:center;gap:6px;margin-top:18px;height:25px;padding:0 10px;background:var(--blue);color:var(--white);font-size:12px;font-weight:500}

/* footer */
.site-footer{color:var(--white)}
.footer{top:3432px;left:0;width:1200px;height:357px;background:var(--footer)}
.f-brand{top:3503px;left:122px;font-family:'Dosis',sans-serif;font-weight:700;font-size:24px;color:var(--white)}
.f-text{top:3578px;left:107px;width:300px;font-size:13px;line-height:23px;color:var(--white)}
.social{position:absolute;top:3691px;width:25px;height:25px;background:var(--blue)}
.f-col h4{font-size:21px;font-weight:400;margin-bottom:14px}
.f-col li{list-style:none;font-size:13px;line-height:16px;margin-bottom:16px;display:flex;gap:6px}
.f-col li::before{content:"›";color:var(--blue)}
.f-col{position:absolute;top:3503px;color:var(--white)}
.nl-input{top:3576px;left:784px;width:310px;height:44px;border-radius:22px;background:var(--white);color:#888;font-size:13px;line-height:44px;padding-left:18px}
.nl-btn{top:3576px;left:987px;width:107px;height:44px;border-radius:0 22px 22px 0;background:var(--blue);color:var(--white);font-size:13px;line-height:44px;text-align:center}
.badge{top:3646px;left:784px;width:122px;height:83px;background:#1e3a8c;border-bottom:14px solid #e8641c}
.copy{top:3789px;left:0;width:1200px;height:42px;background:var(--blue);color:var(--white);text-align:center;font-size:13px;line-height:42px}
</style>
</head>
<body>

<header>
  <div class="abs topbar">
    <div class="item" style="left:676px">
      <svg width="18" height="13" viewBox="0 0 18 13"><rect x="0.5" y="0.5" width="17" height="12" fill="#222"/><path d="M1 1l8 6 8-6" stroke="#fff" stroke-width="1.4" fill="none"/></svg>
      <span>info@lumavend.de</span>
    </div>
    <div class="item" style="left:866px">
      <svg width="16" height="16" viewBox="0 0 24 24"><path d="M6.6 10.8a15 15 0 006.6 6.6l2.2-2.2a1 1 0 011-.25 11.4 11.4 0 003.6.6 1 1 0 011 1V20a1 1 0 01-1 1A17 17 0 013 4a1 1 0 011-1h3.5a1 1 0 011 1c0 1.25.2 2.45.6 3.6a1 1 0 01-.25 1z" fill="#222"/></svg>
      <span>+49 4000 555 120-0</span>
    </div>
    <div class="lang"><span>DE</span> / EN</div>
  </div>
  <nav class="abs nav">
    <div class="brand">LumaVend</div>
    <a href="#" style="left:706px">Home</a>
    <a href="#" style="left:803px">Pickup Order</a>
    <a href="#" style="left:931px">About Us</a>
    <a href="#" style="left:1027px">Contact Us</a>
  </nav>
</header>

<section class="abs hero"></section>
<div class="abs hero-tag">Want To Purchase New Or Get Older Repaired?</div>
<h1 class="abs hero-title">SUSTAINABLE<br>AND<br>ECONOMICAL</h1>
<p class="abs hero-text">We are always interested in buying used endoscopes, accessories and peripherals from Orvane, Pexlo and Fujaro at fair conditions.</p>
<a class="btn" style="left:107px;top:593px;width:141px">Purchase Request</a>
<a class="btn" style="left:253px;top:593px;width:141px">Repair Request</a>
<div class="photo hero-photo" role="img" aria-label="Photo of a black video endoscope control head with its insertion tube"></div>

<section>
  <div class="feature" style="left:107px"><div class="ic"><svg width="24" height="24" viewBox="0 0 24 24"><circle cx="9" cy="4" r="2.5" fill="#3cb9fc"/><path d="M7 8h4l1 7h-2l-1 6H8l-1-6H6z" fill="#3cb9fc"/><rect x="14" y="14" width="6" height="6" fill="#3cb9fc"/></svg></div><h3>Pickup</h3><p>By qualified team</p></div>
  <div class="feature" style="left:360px"><div class="ic"><svg width="24" height="24" viewBox="0 0 24 24"><rect x="3" y="5" width="16" height="11" rx="2" fill="#3cb9fc"/><rect x="3" y="8" width="16" height="2" fill="#fff"/><circle cx="18" cy="17" r="4" fill="#1ea6f2"/></svg></div><h3>Repair</h3><p>Endoscope repair service</p></div>
  <div class="feature" style="left:613px"><div class="ic"><svg width="24" height="24" viewBox="0 0 24 24"><circle cx="12" cy="12" r="8" fill="none" stroke="#3cb9fc" stroke-width="2.5"/><text x="12" y="16" text-anchor="middle" font-size="10" font-weight="700" fill="#3cb9fc" font-family="Roboto,sans-serif">$</text></svg></div><h3>Sale</h3><p>Used endoscopes</p></div>
  <div class="feature" style="left:865px"><div class="ic"><svg width="24" height="24" viewBox="0 0 24 24"><circle cx="11" cy="11" r="8" fill="#3cb9fc"/><text x="11" y="15" text-anchor="middle" font-size="11" font-weight="700" fill="#fff" font-family="Roboto,sans-serif">?</text></svg></div><h3>Purchase</h3><p>Used endoscop</p></div>
</section>

<section>
  <h2 class="sec-title" style="top:938px">Best Services</h2>
  <p class="sec-sub" style="top:983px">Ut enim ad minim veniam, quis nostrud exercitation ullamco laboris nisi ut aliquip ex ea commodo consequat.</p>

  <div class="photo svc-photo" role="img" aria-label="Photo of an endoscope control body mounted on a stand"></div>

  <svg class="svc-ic" style="left:107px;top:1047px" viewBox="0 0 40 40"><path d="M20 2l16 6v11c0 10-7 16-16 19C11 35 4 29 4 19V8z" fill="#3cb9fc"/><circle cx="20" cy="20" r="9" fill="none" stroke="#fff" stroke-width="2"/><path d="M15 20l4 4 6-7" stroke="#fff" stroke-width="2.2" fill="none"/></svg>
  <div class="svc left" style="top:1047px"><h4>Qualified Products</h4><p>Quis nostrud exercitation ullamco laboris<br>nisi ut commodo consequat.</p></div>
  <svg class="svc-ic" style="left:107px;top:1137px" viewBox="0 0 40 40"><path d="M20 2l16 6v11c0 10-7 16-16 19C11 35 4 29 4 19V8z" fill="#3cb9fc"/><circle cx="20" cy="19" r="7" fill="none" stroke="#fff" stroke-width="3" stroke-dasharray="3 2"/><circle cx="20" cy="19" r="3" fill="#fff"/></svg>
  <div class="svc left" style="top:1137px"><h4>Tested Products</h4><p>Quis nostrud exercitation ullamco laboris<br>nisi ut commodo consequat.</p></div>
  <svg class="svc-ic" style="left:107px;top:1227px" viewBox="0 0 40 40"><rect x="6" y="2" width="26" height="12" rx="3" fill="#3cb9fc"/><circle cx="12" cy="8" r="2" fill="#fff"/><circle cx="19" cy="8" r="2" fill="#fff"/><circle cx="26" cy="8" r="2" fill="#fff"/><circle cx="19" cy="21" r="5" fill="#3cb9fc"/><path d="M9 38c0-7 4-11 10-11s10 4 10 11z" fill="#3cb9fc"/></svg>
  <div class="svc left" style="top:1227px"><h4>Top Rated</h4><p>Quis nostrud exercitation ullamco<br>nisi ut commodo consequat.</p></div>
  <svg class="svc-ic" style="left:107px;top:1317px" viewBox="0 0 40 40"><circle cx="20" cy="21" r="16" fill="#3cb9fc"/><circle cx="20" cy="21" r="11" fill="#fff"/><path d="M20 14v8h6" stroke="#3cb9fc" stroke-width="2.5" fill="none"/><rect x="16" y="1" width="8" height="4" fill="#3cb9fc"/></svg>
  <div class="svc left" style="top:1317px"><h4>Fast Delivery</h4><p>Quis nostrud exercitation ullamco laboris<br>nisi ut commodo consequat.</p></div>

  <div class="svc right" style="top:1047px"><h4>Varified Products</h4><p>Quis nostrud exercitation ullamco laboris<br>nisi ut commodo consequat.</p></div>
  <svg class="svc-ic" style="left:1053px;top:1047px" viewBox="0 0 40 40"><path d="M6 18l14-6 14 6-14 6z" fill="#1ea6f2"/><path d="M6 18v14l14 6V24z" fill="#3cb9fc"/><path d="M34 18v14l-14 6V24z" fill="#7ccffd"/><path d="M20 2v6M8 6l4 4M32 6l-4 4" stroke="#3cb9fc" stroke-width="2.5"/></svg>
  <div class="svc right" style="top:1137px"><h4>Easy Payment</h4><p>Quis nostrud exercitation ullamco laboris<br>nisi ut commodo consequat.</p></div>
  <svg class="svc-ic" style="left:1053px;top:1137px" viewBox="0 0 40 40"><rect x="2" y="6" width="30" height="20" rx="3" fill="#3cb9fc"/><rect x="2" y="11" width="30" height="4" fill="#fff"/><circle cx="32" cy="28" r="7" fill="#1ea6f2"/><path d="M29 28l2 2 4-4" stroke="#fff" stroke-width="2" fill="none"/></svg>
  <div class="svc right" style="top:1227px"><h4>Best Support</h4><p>Quis nostrud exercitation ullamco laboris<br>nisi ut commodo consequat.</p></div>
  <svg class="svc-ic" style="left:1053px;top:1227px" viewBox="0 0 40 40"><circle cx="17" cy="16" r="14" fill="#3cb9fc"/><path d="M24 30c4 2 9 3 14 2-3-2-4-5-4-8" fill="#3cb9fc"/><text x="17" y="22" text-anchor="middle" font-size="17" font-weight="700" fill="#fff" font-family="Roboto,sans-serif">?</text></svg>
  <div class="svc right" style="top:1317px"><h4>Return Policy</h4><p>Quis nostrud exercitation ullamco laboris<br>nisi ut commodo consequat.</p></div>
  <svg class="svc-ic" style="left:1053px;top:1317px" viewBox="0 0 40 40"><path d="M34 14A16 16 0 006 14M6 26a16 16 0 0028 0" stroke="#3cb9fc" stroke-width="3.5" fill="none"/><path d="M34 5v10h-10M6 35V25h10" stroke="#3cb9fc" stroke-width="3" fill="none"/><text x="20" y="25" text-anchor="middle" font-size="13" font-weight="700" fill="#3cb9fc" font-family="Roboto,sans-serif">$</text></svg>
</section>

<section class="abs band" role="img" aria-label="Blue tinted photo of a hospital ward in the background"></section>
<div class="band-col" style="left:101px">
  <svg width="52" height="64" viewBox="0 0 52 64"><path d="M26 62L15 49A24 24 0 1137 49z" fill="none" stroke="#fff" stroke-width="3"/><circle cx="26" cy="15" r="2.6" fill="#fff"/><rect x="24" y="21" width="4" height="16" fill="#fff"/></svg>
  <h2>Provide Best Solution</h2>
  <div class="sub">Always ready to provide the best solution</div>
  <p>Ut enim ad minim veniam, quis nostrud exercitation ullamco laboris nisi ut aliquip ex ea commodo consequat. Duis aute irure dolor in reprehenderit in voluptate velit esse cillum dolore</p>
</div>
<div class="band-col" style="left:607px">
  <svg width="52" height="64" viewBox="0 0 52 64"><path d="M26 62L15 49A24 24 0 1137 49z" fill="none" stroke="#fff" stroke-width="3"/><circle cx="26" cy="15" r="2.6" fill="#fff"/><rect x="24" y="21" width="4" height="16" fill="#fff"/></svg>
  <h2>We Are Here To Assist You</h2>
  <div class="sub">Always ready to provide the best solution</div>
  <p>Ut enim ad minim veniam, quis nostrud exercitation ullamco laboris nisi ut aliquip ex ea commodo consequat. Duis aute irure dolor in reprehenderit in voluptate velit esse cillum dolore</p>
</div>
<div class="abs divider"></div>
<div class="abs diamond"></div>
<h2 class="abs quote-title">Get A Free Quote</h2>
<a class="abs quote-btn">Get A Qoute</a>

<section class="abs reviews"></section>
<h2 class="sec-title" style="top:2143px">Customer Review</h2>
<p class="sec-sub" style="top:2189px">Ut enim ad minim veniam, quis nostrud exercitation ullamco laboris nisi ut aliquip ex ea commodo consequat.</p>
<div class="review" style="left:114px">Ut enim ad minim veniam, quis nostrud exercitation ullamco laboris nisi ut aliquip ex ea commodo consequat. Duis aute irure dolor in reprehenderit in voluptate velit esse cillum dolore.</div>
<div class="review" style="left:621px">Ut enim ad minim veniam, quis nostrud exercitation ullamco laboris nisi ut aliquip ex ea commodo consequat. Duis aute irure dolor in reprehenderit in voluptate velit esse cillum dolore.</div>
<div class="avatar" style="left:164px;background:linear-gradient(#c9d3dc,#3c4a5e)" role="img" aria-label="Portrait photo of a reviewer in a suit"></div>
<div class="rname" style="left:312px">Jonas Merkel</div>
<div class="rrole" style="left:313px">Manager</div>
<div class="avatar" style="left:671px;background:linear-gradient(#eef2f5,#b9c3cc)" role="img" aria-label="Portrait photo of a reviewer in a doctor's coat"></div>
<div class="rname" style="left:819px">Jonas Merkel</div>
<div class="rrole" style="left:820px">Manager</div>
<div class="abs arrow" style="left:573px">&larr;</div>
<div class="abs arrow" style="left:619px">&rarr;</div>

<section>
  <h2 class="sec-title" style="top:2739px">Latest Update</h2>
  <p class="sec-sub" style="top:2785px">Ut enim ad minim veniam, quis nostrud exercitation ullamco laboris nisi ut aliquip ex ea commodo consequat.</p>
  <article class="post" style="left:114px">
    <div class="img" style="background:linear-gradient(135deg,#e4ecf2,#9fb3c4)" role="img" aria-label="Photo of a nurse with a clipboard next to a hospital bed"></div>
    <div class="body"><div class="date">25 May 2020</div><h3>Quis nostrud exercitation ullamco</h3><p>Ut enim ad minim veniam, quis nostrud exercitation ullamco laboris nisi ut aliquip ex ea commodo consequat.</p><span class="share">&lt; Share</span></div>
  </article>
  <article class="post" style="left:452px">
    <div class="img" style="background:linear-gradient(135deg,#f0c24a,#e0a020)" role="img" aria-label="Photo of a person holding a face mask against a yellow wall"></div>
    <div class="body"><div class="date">25 May 2020</div><h3>Quis nostrud exercitation ullamco</h3><p>Ut enim ad minim veniam, quis nostrud exercitation ullamco laboris nisi ut aliquip ex ea commodo consequat.</p><span class="share">&lt; Share</span></div>
  </article>
  <article class="post" style="left:790px">
    <div class="img" style="background:linear-gradient(135deg,#f4f6f8,#c8d3dc)" role="img" aria-label="Photo of a doctor with a stethoscope in a bright clinic"></div>
    <div class="body"><div class="date">25 May 2020</div><h3>Quis nostrud exercitation ullamco</h3><p>Ut enim ad minim veniam, quis nostrud exercitation ullamco laboris nisi ut aliquip ex ea commodo consequat.</p><span class="share">&lt; Share</span></div>
  </article>
</section>

<footer class="site-footer">
  <div class="abs footer"></div>
  <div class="abs f-brand">LumaVend</div>
  <p class="abs f-text">Ut enim ad minim veniam, quis nostrud exercitation ullamco laboris nisi ut aliquip ex ea commodo consequat quis nostrud exercitation ullamco laboris.</p>
  <div class="social" style="left:107px"></div>
  <div class="social" style="left:146px"></div>
  <div class="social" style="left:184px"></div>
  <div class="f-col" style="left:445px">
    <h4>Categories</h4>
    <ul><li>Endoscope Repair</li><li>Used Endoscopes</li><li>Endoscopy Systems</li><li>Endoscopy<br>Accessories</li><li>Purchase</li></ul>
  </div>
  <div class="f-col" style="left:614px">
    <h4>Usefull links</h4>
    <ul><li>About</li><li>Services</li><li>Privacy Policy</li><li>Statements</li><li>Faq</li></ul>
  </div>
  <div class="f-col" style="left:784px">
    <h4>Newsletter</h4>
    <div style="font-size:13px">Sign up for our newsletter</div>
  </div>
  <div class="abs nl-input">Enter your email</div>
  <div class="abs nl-btn">Subscribe</div>
  <div class="abs badge" role="img" aria-label="Quality certification badge"></div>
  <div class="abs copy">Copyright © 2022 LumaVend. All Rights Reserverd.</div>
</footer>

</body>
</html>
```